New look and feel for investment website

Hi

Our website needs a crisp and professional look and feel applying to it. Here’s the address: http://www.brightplinth.co.uk. Since posting the brief yesterday (Tuesday, 16 August), we've reduced the amount of content on the home page, which should make life a little easier for you. We will come back later today, with some points of reference in terms of sites we like the look of. (See below)

17 August, 1.20pm GMT. OK, comments generally on the designs submitted so far. Please keep in mind that images of graphs, piles of coins, paper money and pretty females are not what is required. Better to think in terms of abstract imagery instead. Ratios? Circles? Relationships? Patterns? Not money,sex,graphs etc. Hope that helps.

For guidance on look and feel, please refer to these sites, which we like:

http://www.morvelle.co.uk/
http://www.qz.com/
https://www.harrowfieldtamsin.com
https://www.pirelconcerns.com
https://www.kvantule.com
Updates

Here's the Tall Beacons logo created in AI CS5.

Our market is professional financial advisers and relatively sophisticated private investors. The look and feel therefore should be slick and sophisticated - not 'lively' and lightweight, more like a banking site. Please read the brief again where we've added a list of websites that we really like the look of to get a better feel for what we're looking for. Thanks once again, we appreciate the work you're putting in.

It's essential that all the elements that are on the current home page be included on all new designs. 

We use a device in our e-mails which you may wish to incorporate in your design.

Target Market(s)

Professional financial advisers. People who know about investment and money.

Industry/Entity Type

Investment

Requirements
Should not have
• Graphs or people.

```html
<!DOCTYPE html>
<html lang="en">
<head>
<meta charset="utf-8">
<title>Tall Beacons</title>
<link href="https://fonts.googleapis.com/css2?family=Roboto:wght@300;400;500;700&display=swap" rel="stylesheet">
<style>
:root{
  --page:#e9ebee;
  --panel:#ffffff;
  --ink:#4b5563;
  --ink-dark:#1c2838;
  --navy:#14263f;
  --navy-mid:#1f3a5c;
  --steel:#3d5a7e;
  --gold:#c39b4e;
  --gold-soft:#e0c48a;
  --line:#d8dde4;
  --tint:#f4f6f9;
}
*{margin:0;padding:0;box-sizing:border-box}
html,body{width:926px;height:1200px;overflow:hidden}
body{background:var(--page);font-family:"Roboto",Arial,sans-serif;color:var(--ink);position:relative}
a{color:inherit}
.top-links{position:absolute;top:15px;right:29px;font-size:10px;color:var(--ink-dark)}
.top-links span{margin:0 5px;color:#9aa3ae}
.panel{position:absolute;left:29px;top:43px;width:868px;height:1024px;background:var(--panel);border-radius:6px;box-shadow:0 1px 3px rgba(20,38,63,.08)}
.logo{position:absolute;left:24px;top:26px;display:flex;align-items:center;gap:8px}
.logo-name{font-size:40px;font-weight:300;color:var(--navy);letter-spacing:-.5px}
.logo-dot{width:8px;height:8px;background:var(--gold);margin-top:12px}
.register-btn{position:absolute;left:627px;top:22px;width:230px;height:52px;border-radius:4px;background:var(--navy);display:flex;align-items:center;text-decoration:none}
.register-icon{margin-left:18px;width:30px;height:30px;border:1.5px solid var(--gold-soft);border-radius:50%;display:flex;align-items:center;justify-content:center}
.register-label{margin-left:14px;font-size:15px;font-weight:500;color:#fff;letter-spacing:.3px}
.hero{position:absolute;left:12px;top:96px;width:843px;height:212px;border-radius:4px;overflow:hidden;background:linear-gradient(100deg,var(--navy) 0%,var(--navy-mid) 55%,var(--steel) 100%)}
.hero-art{position:absolute;inset:0;background:radial-gradient(circle at 50% 30%,rgba(224,196,138,.45) 0,rgba(224,196,138,.12) 22%,transparent 42%)}
.hero-rule{position:absolute;left:22px;top:140px;width:46px;height:2px;background:var(--gold)}
.hero-title{position:absolute;left:22px;top:150px;right:30px;font-size:21px;line-height:27px;font-weight:300;color:#fff}
.news{position:absolute;left:12px;top:328px;width:843px;height:43px;border-radius:4px;background:var(--tint);border:1px solid var(--line);display:flex;align-items:center;overflow:hidden}
.news-arrow{width:18px;height:100%;background:#e3e7ed;display:flex;align-items:center;justify-content:center}
.news-text{flex:1;padding:0 8px;font-size:11px;white-space:nowrap;overflow:hidden;color:var(--ink)}
.news-text b{color:var(--navy);font-weight:700}
.side-nav{position:absolute;left:11px;top:388px;width:228px;height:269px;border:1px solid var(--line);border-radius:4px;background:var(--tint);padding:20px 0 0 12px}
.side-nav li{list-style:none;font-size:10px;line-height:22px;color:var(--ink-dark);white-space:nowrap}
.side-nav li::before{content:"›";color:var(--gold);margin-right:7px;font-weight:700}
.promo{position:absolute;left:11px;top:678px;width:228px;height:260px;border-radius:4px;background:linear-gradient(160deg,var(--navy),var(--navy-mid));border-top:3px solid var(--gold);padding:26px 16px;text-align:center;font-size:16px;line-height:26px;font-weight:500;color:#fff}
.promo a{color:var(--gold-soft);font-weight:700}
.content{position:absolute;left:257px;top:385px;width:590px;font-size:11px;line-height:21.7px;color:var(--ink)}
.content h2{font-size:11px;font-weight:700;color:var(--ink-dark)}
.content p{margin-bottom:21.7px}
.content .lead{font-weight:700;color:var(--navy)}
.content .summary{color:var(--steel)}
.content .summary a{color:var(--navy)}
.footer{position:absolute;left:33px;top:1078px;width:860px;font-size:9.5px;line-height:12.6px;color:#4b5563}
.footer p{margin-bottom:13px}
</style>
</head>
<body>
<nav class="top-links"><a>Login</a><span>|</span><a>Register for free</a><span>|</span><a>Contact us</a><span>|</span><a>Terms &amp; Conditions</a></nav>

<main class="panel">
  <div class="logo"><span class="logo-name">Tall Beacons</span><span class="logo-dot"></span></div>
  <a class="register-btn"><span class="register-icon"><svg width="14" height="14"><path d="M7 1v12M1 7h12" stroke="#e0c48a" stroke-width="1.6"/></svg></span><span class="register-label">Free Registration</span></a>

  <section class="hero">
    <div class="hero-art" role="img" aria-label="Abstract image of a glowing light bulb held in cupped hands"></div>
    <span class="hero-rule"></span>
    <h1 class="hero-title">A potential return of 23.57 % a year from America's biggest businesses with the emphasis firmly on capital preservation.</h1>
  </section>

  <div class="news">
    <span class="news-arrow"><svg width="8" height="10"><path d="M6 1 2 5l4 4" stroke="#14263f" stroke-width="1.6" fill="none"/></svg></span>
    <p class="news-text"><b>Recent News:</b> Average, annualised compound return over to : 23.57 %. So far this year, the portfolio's return is 13.49 %. Worst ever annual loss: -1.48 %; best ever</p>
    <span class="news-arrow"><svg width="8" height="10"><path d="M2 1l4 4-4 4" stroke="#14263f" stroke-width="1.6" fill="none"/></svg></span>
  </div>

  <ul class="side-nav">
    <li>Home</li><li>Two Minute Guide</li><li>Current &amp; year to date performance</li><li>Watch list</li><li>Other key numbers</li><li>Back tested results</li><li>History of all trades</li><li>FAQs</li><li>About our analyses</li><li>About value investing</li><li>The Halden 1000 and the Marlow 500 index</li>
  </ul>

  <aside class="promo">Free trial period: if you would like to monitor the portfolio's performance for six months free of charge then please <a href="#">complete the registration form.</a></aside>

  <article class="content">
    <h2>Something different...</h2>
    <p>You may well be thinking that Tall Beacons is just another one of those banal share recommendation sites sprinkled with the usual idiotic and patronising platitudes, gross exaggerations, silly get-rich-quick promises and all the other stuff and nonsense you associate with the black art of share-tipping...</p>
    <p class="lead">Well, we have a pleasant surprise for you: you couldn't be further from the truth.</p>
    <h2>No! No! No!</h2>
    <p>There's no newsletter to read, books to study, dvds to watch or traders' secrets to be revealed. No never-ending stream of recommendations. No webcasts. No effort or time to invest. No training. No research. No tedious market commentaries. And no financial discomfort for you whatsoever. (At least for the first six months that is!)</p>
    <h2>Undervalued and overlooked</h2>
    <p>Our program finds stocks that appear to be undervalued - i.e., where the price of a company's share does not reflect the real worth of the business. We confine our search to 1,000 of the USA's biggest companies; successful, robust, large cap businesses, which for one reason or another are either unpopular with investors or overlooked by them</p>
    <h2>We don't get it right every time...</h2>
    <p>We do however, get it right 75.58 % of the time (the total of all our winning trades out of all our trades) and on that basis tracking our portfolio should produce an average return of 23.57 % a year for you.</p>
    <h2>An average of five trades a year and never more than five holdings.</h2>
    <p>We tested different numbers of holdings and capital allocation percentages. The best results came from a portfolio of no more than five holdings with the same amount of capital allocated to each holding. That's it. You don't have to do it that way, but it works for us.</p>
    <p class="summary">For a succinct explanation of our service and the results to date...<a href="#">please go here</a></p>
    <p><a href="#">More about the strategy we use to choose stocks...</a></p>
  </article>
</main>

<footer class="footer">
  <p>If you have any questions, please e-mail <a href="#">info@tallbeacons.co.uk</a>. Although we're very willing to answer queries about the way we pick stocks, please do keep in mind that as we're giving this service away free of charge initially, we're not inclined to expend time and energy debating the relative merits of value investing or fundamental analyses. Other than that, fire away!</p>
  <p>This website is published by Tall Beacons Ltd. Registered in England No. 08341927. Registered office: 48 Alder Crescent London N9 2QT. This website and its content is the copyright of Tall Beacons Ltd - © Tall Beacons Ltd 2011. All rights reserved. Any redistribution or reproduction of part or all of the contents in any form is prohibited other than the following: you may print or download to a local hard disk extracts for your personal and non-commercial use only you may copy the content to individual third parties for their personal use, but only if you acknowledge the website as the source of the material. You may not, except with our express written permission, distribute or commercially exploit the content. Nor may you transmit it or store it in any other website or other form of electronic retrieval system.</p>
</footer>
</body>
</html>
```